Vell Studio - Lash Serum Packaging

Need Packaging done for this Lash Serum for a brand called "Vell Studio". The bottle will remain black but the box can be any color. This will be for a 3ml bottle. Give me different options for packaging that is minimalist and clean for this brand that makes it look expensive and make people want to buy.

```html
<!DOCTYPE html>
<html lang="en">
<head>
<meta charset="utf-8">
<title>Vell Studio – Lash Serum Box Dieline</title>
<link href="https://fonts.googleapis.com/css2?family=Poppins:ital,wght@0,300;0,400;0,600;1,300;1,400&family=Dancing+Script:wght@500&display=swap" rel="stylesheet">
<style>
  :root {
    --paper: #ffffff;
    --box-black: #060606;
    --cut-teal: #2f8190;
    --fold-magenta: #d0157f;
    --band-pink: #f7c5d7;
    --band-text: #d47c9f;
    --accent-pink: #f6cfdc;
    --ink-white: #ffffff;
    --ghost: #1b1b1b;
    --ghost-light: #d8d8d8;
  }
  html, body {
    margin: 0;
    padding: 0;
    width: 921px;
    height: 1200px;
    overflow: hidden;
    background: var(--paper);
  }
  .dieline {
    display: block;
    width: 921px;
    height: 1200px;
  }
  .die-body { fill: var(--box-black); }
  .cut-line { fill: none; stroke: var(--cut-teal); stroke-width: 1.5; }
  .fold-line { fill: none; stroke: var(--fold-magenta); stroke-width: 1.5; }
  .rule { stroke: var(--ink-white); stroke-width: 1.5; }
  .band { fill: var(--band-pink); }
  .brand-name {
    font-family: "Poppins", sans-serif;
    font-weight: 400;
    fill: var(--ink-white);
  }
  .brand-name.on-band { fill: var(--band-text); }
  .tagline {
    font-family: "Dancing Script", cursive;
    font-weight: 500;
    fill: var(--ink-white);
    font-size: 30px;
  }
  .product-label {
    font-family: "Poppins", sans-serif;
    font-style: italic;
    font-weight: 300;
    fill: var(--ink-white);
    font-size: 18px;
  }
  .band-label {
    font-family: "Poppins", sans-serif;
    font-weight: 300;
    fill: var(--band-text);
    font-size: 18px;
  }
  .band-label.italic { font-style: italic; }
  .body-copy {
    font-family: "Poppins", sans-serif;
    font-weight: 300;
    fill: var(--ink-white);
    font-size: 12.6px;
  }
  .body-copy .lead { font-weight: 600; font-size: 15px; }
  .tagline-frame { fill: none; stroke: var(--ink-white); stroke-width: 2; }
</style>
</head>
<body>
<svg class="dieline" viewBox="0 0 921 1200" xmlns="http://www.w3.org/2000/svg">

  <!-- die shape: outer black -->
  <g class="die-body">
    <polygon points="0,283 66,266 66,932 0,915"/>
    <path d="M66,280 V38 Q66,0 104,0 H266 Q304,0 304,38 V280 Z"/>
    <path d="M287,280 Q300,255 304,230 V185 Q304,159 330,159 H468 Q494,159 498,185 L505,232 Q510,258 522,264 V280 Z"/>
    <path d="M700,280 Q708,252 710,235 V185 Q712,159 740,159 H885 Q912,159 914,185 V258 Q921,268 921,280 Z"/>
    <rect x="60" y="262" width="861" height="673"/>
    <path d="M274,921 V1000 Q276,1040 318,1046 H478 V921 Z"/>
    <path d="M478,921 V1160 Q478,1200 518,1200 H675 Q715,1200 715,1160 V921 Z"/>
    <path d="M715,921 V1000 Q720,1040 760,1040 H888 Q921,1040 921,1000 V921 Z"/>
  </g>

  <!-- cut lines -->
  <g class="cut-line">
    <polygon points="15,296 81,280 81,920 15,905"/>
    <path d="M81,278 V48 Q81,15 114,15 H254 Q287,15 287,48 V278"/>
    <line x1="81" y1="70" x2="287" y2="70"/>
    <path d="M295,278 Q306,266 310,245 V190 Q310,174 326,174 H470 Q486,174 488,190 L491,240 Q493,266 494,278"/>
    <path d="M708,278 Q716,265 718,245 V190 Q718,174 734,174 H876 Q892,174 892,190 V262 Q900,272 905,278"/>
    <path d="M287,921 V990 Q290,1028 326,1032 H470 Q478,1030 478,1020"/>
    <path d="M494,921 V1160 Q494,1183 517,1183 H677 Q700,1183 700,1160 V921"/>
    <line x1="494" y1="1125" x2="700" y2="1125"/>
    <path d="M715,935 Q722,950 722,990 Q726,1024 762,1026 H880 Q905,1024 905,995 V921"/>
  </g>

  <!-- short fold marks on tuck flaps -->
  <line class="fold-line" x1="112" y1="75" x2="255" y2="75"/>
  <line class="fold-line" x1="525" y1="1125" x2="667" y2="1125"/>

  <!-- faint figure artwork behind the panels -->
  <rect role="img" aria-label="Faint seated figure silhouettes decoration" x="218" y="435" width="592" height="427" rx="120" fill="var(--ghost)"/>

  <!-- top flap brand name, upside down -->
  <text class="brand-name" font-size="26" text-anchor="middle" transform="rotate(180 184 165)" x="184" y="174">Vell Studio</text>

  <!-- panel 1: pink wedge pattern -->
  <polygon role="img" aria-label="Pink wavy line pattern" points="81,278 287,278 287,292 190,356 81,292" fill="var(--accent-pink)"/>

  <!-- panel 1: tagline frame -->
  <path class="tagline-frame" d="M232,565 V470 Q232,455 217,455 H141 Q126,455 126,470 V728 Q126,743 141,743 H217 Q232,743 232,728 V682"/>
  <text class="tagline" x="136" y="597">Nourish</text>
  <text class="tagline" x="228" y="636" font-size="26">&amp;</text>
  <text class="tagline" x="170" y="670">Grow</text>

  <!-- panel 2: vertical brand name -->
  <text class="brand-name" font-size="46" text-anchor="middle" transform="rotate(-90 440 490)" x="440" y="506">Vell Studio</text>

  <!-- panel 3: eye artwork -->
  <rect role="img" aria-label="Closed eye with brow and lashes line illustration" x="556" y="332" width="80" height="64" rx="22" fill="var(--ghost-light)"/>

  <!-- panel 4: body copy -->
  <text class="body-copy" x="724">
    <tspan x="724" y="353"><tspan class="lead">Lorem ipsum</tspan> dolor</tspan>
    <tspan x="724" y="371">sit amet, consectetuer</tspan>
    <tspan x="724" y="388">adipiscing elit, sed diam</tspan>
    <tspan x="724" y="406">nonummy nibh euismod</tspan>
    <tspan x="724" y="423">tincidunt ut laoreet</tspan>
    <tspan x="724" y="441">dolore magna aliquam</tspan>
    <tspan x="724" y="458">erat volutpat. Ut Lorem</tspan>
    <tspan x="724" y="475">ipsum dolor sit amet,</tspan>
    <tspan x="724" y="493">consectetuer adipiscing</tspan>
    <tspan x="724" y="510">elit, sed diam nonummy</tspan>
    <tspan x="724" y="528">nibh euismod tincidunt</tspan>
    <tspan x="724" y="545">ut laoreet dolore magna</tspan>
    <tspan x="724" y="563">aliquam erat volutpat. Ut</tspan>
    <tspan x="724" y="580">Lorem ipsum dolor sit</tspan>
    <tspan x="724" y="597">amet, consectetuer</tspan>
  </text>
  <text class="brand-name" font-size="26" text-anchor="middle" x="802" y="768">Vell Studio</text>

  <!-- product line -->
  <line class="rule" x1="124" y1="812" x2="308" y2="812"/>
  <text class="product-label" text-anchor="middle" x="390" y="820">Lash Serum</text>
  <line class="rule" x1="472" y1="812" x2="869" y2="812"/>

  <!-- bottom band -->
  <rect class="band" x="81" y="865" width="824" height="56"/>
  <text class="brand-name on-band" font-size="15" text-anchor="middle" x="184" y="898">Vell Studio</text>
  <text class="band-label" text-anchor="middle" x="390" y="900">3ml</text>
  <text class="brand-name on-band" font-size="15" text-anchor="middle" x="597" y="898">Vell Studio</text>
  <text class="band-label italic" text-anchor="middle" x="802" y="900">Lash Serum</text>

  <!-- panel fold lines -->
  <g class="fold-line">
    <rect x="81" y="278" width="824" height="643"/>
    <line x1="287" y1="278" x2="287" y2="921"/>
    <line x1="494" y1="278" x2="494" y2="921"/>
    <line x1="700" y1="278" x2="700" y2="921"/>
  </g>
</svg>
</body>
</html>
```